Steel Rebar Fabrication Company needs Facebook Ads & page, Instagram Ads & pages designed.

I want to put out an Instagram, Facebook ad, and LinkedIn campaign out for my new company, Ridgeline Metals Inc. I want the ads to be short but clean, clear and precise. I want our address: 4817 Marlowe Dr. Tsawwassen, BC. I want our hours of operation to be listed 8:00am to 4:00pm Monday to Friday. Product Delivery to your job site or pick up at our yard available. We can cut, bend to custom and standard shapes based upon Canadian CSA Standards. We offer products ranging from 10mm to 35mm diameter Grade 400W rebar. We can bend stirrups, dowels, hairpins; whatever your company needs to complete your product. Whether it is a small project, Tilt Up warehouse, Wood Frame Construction with Concrete parkade foundation; we have the team to meet your needs.
Email address: info@ridgelinemetalsinc.ca
We can service all areas of British Columbia.

Target Market(s)

Construction Company's for homes, condominiums, warehouses, commercial, industrial, and infrastructure projects. As well, as the every day DIY home improvement or renovator.

Industry/Entity Type

Construction

Requirements
Nice to have
• Would like to see a image of the rebar steel that I have provided in the ad. Even if it is in the background with a lower opacity level. Bonus if someone includes any of the movie files I have uploaded.

```html
<!DOCTYPE html>
<html lang="en">
<head>
<meta charset="utf-8">
<title>Ridgeline Metals Inc. — Need Steelwork?</title>
<link rel="stylesheet" href="https://fonts.googleapis.com/css2?family=Montserrat:wght@700;800&family=Lato:wght@400&display=swap">
<style>
  :root {
    --ink: #1a1a1a;
    --text: #222222;
    --bg-light: #ffffff;
    --bg-grey: #b4b4b4;
    --disc: #bdb9b9;
    --steel-light: #f2f2f2;
    --steel-mid: #d6d6d6;
  }
  html, body {
    margin: 0;
    padding: 0;
    width: 1200px;
    height: 1200px;
    overflow: hidden;
  }
  .ad {
    position: relative;
    width: 1200px;
    height: 1200px;
    overflow: hidden;
    background: linear-gradient(100deg, var(--bg-grey) 0%, #dcdcdc 30%, var(--bg-light) 62%, var(--bg-light) 100%);
    color: var(--text);
  }
  .brand {
    position: absolute;
    left: 61px;
    top: 82px;
    display: flex;
    align-items: center;
    gap: 16px;
    font-family: "Montserrat", sans-serif;
    font-weight: 800;
    font-size: 40px;
    letter-spacing: 0.5px;
    color: var(--ink);
  }
  .brand-dot {
    width: 30px;
    height: 30px;
    border-radius: 50%;
    background: var(--ink);
  }
  .rebar-visual {
    position: absolute;
    left: 520px;
    top: 0;
    width: 680px;
    height: 410px;
    background: radial-gradient(ellipse at 60% 40%, var(--steel-mid) 0%, var(--steel-light) 45%, rgba(255,255,255,0) 72%);
  }
  .headline {
    position: absolute;
    left: 54px;
    top: 268px;
    margin: 0;
    font-family: "Montserrat", sans-serif;
    font-weight: 800;
    font-size: 140px;
    line-height: 122px;
    letter-spacing: 1px;
    color: var(--ink);
  }
  .subhead {
    position: absolute;
    left: 58px;
    top: 545px;
    width: 1100px;
    margin: 0;
    font-family: "Montserrat", sans-serif;
    font-weight: 700;
    font-size: 34px;
    line-height: 40px;
    color: var(--ink);
  }
  .features {
    position: absolute;
    left: 57px;
    top: 722px;
    margin: 0;
    padding: 0;
    list-style: none;
    font-family: "Lato", sans-serif;
    font-size: 32px;
    line-height: 62px;
    color: var(--text);
  }
  .features li::before {
    content: "> ";
  }
  .accent-disc {
    position: absolute;
    left: 578px;
    top: 884px;
    width: 588px;
    height: 588px;
    border-radius: 50%;
    background: var(--disc);
  }
  .contact {
    position: absolute;
    right: 56px;
    top: 962px;
    margin: 0;
    text-align: right;
    font-family: "Lato", sans-serif;
    font-style: normal;
    font-size: 31px;
    line-height: 49px;
    color: var(--text);
  }
  .contact .email {
    display: block;
    margin-top: 43px;
  }
</style>
</head>
<body>
  <main class="ad">
    <div class="rebar-visual" role="img" aria-label="Coiled steel rebar bent into a spring shape"></div>

    <div class="brand">
      <span class="brand-dot"></span>
      <span class="brand-name">Ridgeline Metals Inc.</span>
    </div>

    <h1 class="headline">NEED<br>STEELWORK?</h1>

    <p class="subhead">We will help you cut / bend to custom / standard shapes based upon Canadian CSA Standards</p>

    <ul class="features">
      <li>Products ranging from 10mm to 35mm diameter Grade 400W rebar</li>
      <li>Product Delivery to your job site / pick up at our yard available</li>
      <li>Service all areas of British Columbia</li>
    </ul>

    <div class="accent-disc"></div>

    <address class="contact">
      4817 Marlowe Dr. Tsawwassen, BC.<br>
      Available 8:00am - 4:00pm Mon- Fri
      <span class="email">info@ridgelinemetalsinc.ca</span>
    </address>
  </main>
</body>
</html>
```